Geschäftspapiere für Unternehmens- und Personalberatung
Zielgruppe
Unternehmens- und Personalberatung für Fach- und Führungskräfte, Zielgruppe meistens Akademiker*innen und Diplomingenieur*innen
Aufgabenstellung
nicht verschnörkelt, soll Menschen mit Jahresgehältern über 100.000 EUR ansprechen und seriös wirken

```html
<!DOCTYPE html>
<html lang="de">
<head>
<meta charset="utf-8">
<title>Velqoran – Geschäftsausstattung</title>
<link rel="stylesheet" href="https://fonts.googleapis.com/css2?family=Source+Sans+3:ital,wght@0,400;0,600;0,700;1,400&family=Roboto+Condensed:wght@400;700&display=swap">
<style>
  :root {
    --teal: #006787;
    --slate: #7a9097;
    --ink: #4a4a4a;
    --black: #111;
    --paper: #ffffff;
    --backdrop: #222324;
    --body-font: "Source Sans 3", Arial, sans-serif;
    --info-font: "Roboto Condensed", "Arial Narrow", sans-serif;
  }
  * { box-sizing: border-box; margin: 0; padding: 0; }
  html, body { width: 1200px; height: 800px; overflow: hidden; background: var(--backdrop); }
  .canvas { position: relative; width: 1200px; height: 800px; }
  .sheet { position: absolute; background: var(--paper); overflow: hidden; }
  .fill { position: absolute; inset: 0; width: 100%; height: 100%; }
  .swoosh { position: absolute; left: 0; bottom: 0; width: 100%; }

  /* brand mark */
  .brand { position: absolute; display: flex; align-items: flex-start; gap: 6px; }
  .brand-square { background: var(--slate); flex: none; }
  .brand-text { display: flex; flex-direction: column; align-items: flex-end; }
  .brand-name { font-family: var(--body-font); font-weight: 700; color: var(--teal); line-height: 1; letter-spacing: .5px; }
  .brand-tag { font-family: var(--body-font); color: var(--slate); line-height: 1; margin-top: 1px; }

  /* letterhead */
  .letterhead { left: 59px; top: 28px; width: 487px; height: 752px; }
  .letterhead .brand { left: 43px; top: 46px; }
  .letterhead .brand-square { width: 32px; height: 32px; margin-top: 2px; }
  .letterhead .brand-name { font-size: 31px; }
  .letterhead .brand-tag { font-size: 9px; }

  .owner { position: absolute; font-family: var(--info-font); }
  .owner-icon { position: absolute; left: 0; top: 0; }
  .owner-name { font-weight: 700; color: var(--black); border-bottom: 1px solid var(--teal); line-height: 1.15; }
  .owner-address { color: var(--ink); }
  .letterhead .owner { left: 270px; top: 27px; width: 173px; }
  .letterhead .owner-icon { width: 24px; height: 24px; }
  .letterhead .owner-name { margin-left: 32px; font-size: 17px; padding-bottom: 1px; }
  .letterhead .owner-address { margin-left: 32px; font-size: 11.5px; margin-top: 4px; }

  .letter-body { position: absolute; left: 34px; top: 145px; width: 405px; font-family: var(--body-font); font-size: 11.7px; line-height: 15.1px; color: var(--ink); text-align: justify; }
  .letter-body p + p { margin-top: 15px; }
  .letter-body .salutation { margin-left: 6px; margin-bottom: 15px; }

  .contact-list { position: absolute; list-style: none; font-family: var(--info-font); color: var(--black); }
  .contact-list li { display: flex; align-items: center; }
  .contact-list svg { flex: none; }
  .letterhead .contact-list { left: 34px; top: 638px; font-size: 9.5px; }
  .letterhead .contact-list li { height: 16px; margin-bottom: 11.5px; gap: 4px; }
  .letterhead .contact-list svg { width: 16px; height: 16px; }

  .legal { position: absolute; left: 218px; top: 640px; font-family: var(--info-font); font-size: 8.6px; line-height: 11.8px; color: var(--black); }
  .legal p + p { margin-top: 12px; }
  .letterhead .swoosh { height: 110px; }

  /* business card front */
  .card-front { left: 575px; top: 38px; width: 270px; height: 155px; }
  .card-front .owner { left: 19px; top: 32px; width: 112px; }
  .card-front .owner-icon { top: 6px; width: 14px; height: 14px; }
  .card-front .owner-name { margin-left: 20px; font-size: 12.5px; }
  .card-front .owner-address { margin-left: 20px; font-size: 9.5px; margin-top: 1px; }
  .card-front .brand { left: 161px; top: 34px; gap: 4px; }
  .card-front .brand-square { width: 20px; height: 20px; margin-top: 1px; }
  .card-front .brand-name { font-size: 16.5px; }
  .card-front .brand-tag { font-size: 4.6px; }
  .card-front .contact-list { left: 4px; top: 89px; font-size: 10.5px; }
  .card-front .contact-list li { height: 14px; margin-bottom: 4.5px; gap: 10px; }
  .card-front .contact-list svg { width: 13px; height: 13px; }
  .card-front .contact-list .no-icon { padding-left: 23px; }

  /* business card back */
  .card-back { left: 870px; top: 38px; width: 270px; height: 155px; }
  .card-back .brand { left: 73px; top: 55px; }
  .card-back .brand-square { width: 33px; height: 33px; }
  .card-back .brand-name { font-size: 27px; }
  .card-back .brand-tag { font-size: 8px; }

  /* envelope back */
  .envelope-back { left: 568px; top: 222px; width: 582px; height: 270px; }
  .flap-name { position: absolute; left: 0; right: 0; top: 20px; text-align: center; font-family: var(--body-font); font-weight: 700; font-size: 20px; color: var(--paper); letter-spacing: .5px; }

  /* envelope front */
  .envelope-front { left: 568px; top: 512px; width: 582px; height: 268px; }
  .envelope-front .brand { left: 398px; top: 32px; }
  .envelope-front .brand-square { width: 33px; height: 33px; margin-top: 1px; }
  .envelope-front .brand-name { font-size: 29px; }
  .envelope-front .brand-tag { font-size: 8.5px; }
  .envelope-front .contact-list { left: 11px; top: 155px; font-size: 12px; }
  .envelope-front .contact-list li { height: 18px; margin-bottom: 13px; gap: 6px; }
  .envelope-front .contact-list svg { width: 18px; height: 18px; }
  .envelope-front .swoosh { height: 107px; }
</style>
</head>
<body>
<svg width="0" height="0" style="position:absolute" aria-hidden="true">
  <defs>
    <symbol id="icon-person" viewBox="0 0 24 24">
      <rect x="1" y="1" width="22" height="22" rx="2" fill="#fff" stroke="#006787" stroke-width="2"/>
      <circle cx="12" cy="9" r="4" fill="#006787"/>
      <path d="M4.5 21c0-4.5 3.4-7 7.5-7s7.5 2.5 7.5 7z" fill="#006787"/>
    </symbol>
    <symbol id="icon-person-solid" viewBox="0 0 24 24">
      <rect x="0" y="0" width="24" height="24" rx="2" fill="#006787"/>
      <circle cx="12" cy="9" r="4" fill="#fff"/>
      <path d="M4.5 21c0-4.5 3.4-7 7.5-7s7.5 2.5 7.5 7z" fill="#fff"/>
    </symbol>
    <symbol id="icon-phone" viewBox="0 0 24 24">
      <rect x="1" y="1" width="22" height="22" rx="3" fill="#fff" stroke="currentColor" stroke-width="1.6"/>
      <path d="M7 5.5l2.5-.5 1.6 3.6-1.6 1.2c.8 1.9 2 3.1 3.7 4l1.3-1.5 3.5 1.7-.5 2.5c-6.3.6-11.1-5-10.5-11z" fill="currentColor"/>
    </symbol>
    <symbol id="icon-globe" viewBox="0 0 24 24">
      <rect x="1" y="1" width="22" height="22" rx="3" fill="#fff" stroke="currentColor" stroke-width="1.6"/>
      <circle cx="12" cy="12" r="7.5" fill="currentColor"/>
      <path d="M9 7.5c2 1 1 2.5 2.5 3s1 2.5-1 3-1 3 1 3.5M14 6.5c-1 1.5.5 2 1.5 2.5s2 1 1.5 3" fill="none" stroke="#fff" stroke-width="1.3"/>
    </symbol>
    <symbol id="icon-mail" viewBox="0 0 24 24">
      <rect x="1" y="1" width="22" height="22" rx="3" fill="#fff" stroke="currentColor" stroke-width="1.6"/>
      <path d="M4 17l15-10-4 12-3-4z" fill="currentColor"/>
      <path d="M4 18.5h16" stroke="currentColor" stroke-width="1.4"/>
    </symbol>
  </defs>
</svg>

<main class="canvas">

  <!-- Letterhead -->
  <section class="sheet letterhead" aria-label="Briefbogen">
    <div class="brand">
      <span class="brand-square"></span>
      <div class="brand-text">
        <span class="brand-name">Velqoran</span>
        <span class="brand-tag">Personalberatung</span>
      </div>
    </div>

    <div class="owner">
      <svg class="owner-icon"><use href="#icon-person"/></svg>
      <p class="owner-name">The Owner</p>
      <p class="owner-address">Your Full Address</p>
    </div>

    <div class="letter-body">
      <p class="salutation">orem ipsum dolor sit amet,</p>
      <p>scelerisque. Nam sapien odio, posuere ut ornare eget, sodales eget nibh. Nunc sed nunc lectus. Donec pharetra lobortis nulla, sit amet laoreet mauris ultricies at. Nulla tristique dui hendrerit urna rhoncus pellentesque. Cras vestibulum consectetur arcu, nec faucibus odio auctor at. Curabitur id congue ex. In lobortis vel risus quis porttitor. Vestibulum pellentesque quis tellus sed congue. Curabitur tristique posuere massa, id ultrices nulla tempus tincidunt. Vivamus sit amet enim sem. Quisque porta interdum arcu, sed dapibus magna. Praesent facilisis enim ac ante gravida rutrum.</p>
      <p>Phasellus vel lectus aliquam dui elementum lacinia. Donec et orci iaculis, rutrum augue eget, elementum leo. Curabitur congue libero id mi pulvinar porta. Ut varius enim cursus, lobortis leo sed, facilisis mi. Vivamus pellentesque id ipsum pharetra condimentum. Ut vitae commodo tellus. In eget eros sit amet velit tincidunt ornare. Sed mollis dolor eu condimentum mollis. Mauris vel blandit arcu. Aenean nec placerat lectus. Curabitur placerat id tortor nec consectetur. Nunc sed elit purus. Ut tellus eros, ullamcorper tristique odio quis, elementum molestie urna. Class aptent taciti sociosqu ad litora torquent per conubia nostra, per inceptos himenaeos.</p>
      <p>Maecenas iaculis vulputate dignissim. Nullam lorem felis, mattis vel libero a, imperdiet facilisis orci. Nullam facilisis mi eu arcu ultricies, ac sagittis sem tempus. Proin ullamcorper neque eu mi dapibus, vitae consequat lacus aliquet. Proin posuere ex nec tempus faucibus. Aenean scelerisque nisi justo, sit amet cursus leo euismod ut. Morbi maximus, sapien quis tincidunt ornare, quam nibh hendrerit mauris, id ultricies lorem orci vel dui. Phasellus consectetur sapien a risus convallis dapibus. Sed a tempor libero. Nam quis libero ligula. Morbi eget velit eu sapien finibus iaculis nec tincidunt orci. Donec sodales erat laoreet nisl interdum volutpat.</p>
    </div>

    <ul class="contact-list" style="color:#111">
      <li><svg><use href="#icon-phone"/></svg>+49 01 2345 6789</li>
      <li><svg><use href="#icon-globe"/></svg>www.velqoran.de</li>
      <li><svg><use href="#icon-mail"/></svg>post@velqoran.de</li>
    </ul>

    <div class="legal">
      <p>Bank: Bank Name<br>IBAN: DE44 XXXX XXXX XXXX XXXX XX<br>BIC: WEXXXXXXXXX</p>
      <p>Steuer-Nr. XXX/XXXX/XXXX<br>Ust.-ID: DEXXXXXXXXX</p>
    </div>

    <svg class="swoosh" viewBox="0 0 954 215" preserveAspectRatio="none" aria-hidden="true">
      <path d="M0 178 Q520 200 954 80 L954 215 L0 215 Z" fill="var(--teal)"/>
      <path d="M240 170 Q660 150 954 6 L954 66 Q620 160 240 170 Z" fill="var(--slate)"/>
    </svg>
  </section>

  <!-- Business card, front -->
  <section class="sheet card-front" aria-label="Visitenkarte Vorderseite">
    <svg class="fill" viewBox="0 0 270 155" preserveAspectRatio="none" aria-hidden="true">
      <path d="M0 0 H10 V62 Q10 70 18 70 Q21 70 21 78 V155 H0 Z" fill="var(--teal)"/>
      <path d="M128 0 H270 V10 H136 Q128 10 128 2 Z" fill="var(--teal)"/>
    </svg>
    <div class="owner">
      <svg class="owner-icon"><use href="#icon-person-solid"/></svg>
      <p class="owner-name">The Owner</p>
      <p class="owner-address">Your Full Address</p>
    </div>
    <div class="brand">
      <span class="brand-square"></span>
      <div class="brand-text">
        <span class="brand-name">Velqoran</span>
        <span class="brand-tag">Personalberatung</span>
      </div>
    </div>
    <ul class="contact-list" style="color:var(--teal)">
      <li><svg><use href="#icon-phone"/></svg><span style="color:#111">+49 123 4567 890</span></li>
      <li><svg><use href="#icon-mail"/></svg><span style="color:#111">post@velqoran.com</span></li>
      <li class="no-icon" style="color:#111">www.velqoran.com</li>
    </ul>
  </section>

  <!-- Business card, back -->
  <section class="sheet card-back" aria-label="Visitenkarte Rückseite">
    <svg class="fill" viewBox="0 0 270 155" preserveAspectRatio="none" aria-hidden="true">
      <path d="M0 145 H135 Q140 137 150 137 H270 V155 H0 Z" fill="var(--teal)"/>
    </svg>
    <div class="brand">
      <span class="brand-square"></span>
      <div class="brand-text">
        <span class="brand-name">Velqoran</span>
        <span class="brand-tag">Personalberatung</span>
      </div>
    </div>
  </section>

  <!-- Envelope, back -->
  <section class="sheet envelope-back" aria-label="Briefumschlag Rückseite">
    <svg class="fill" viewBox="0 0 1141 528" preserveAspectRatio="none" aria-hidden="true">
      <path d="M0 0 H1141 V38 L568 145 L0 38 Z" fill="var(--teal)"/>
      <path d="M0 490 Q560 510 1141 390 L1141 528 L0 528 Z" fill="var(--teal)"/>
      <path d="M290 484 Q760 462 1141 322 L1141 378 Q760 472 290 484 Z" fill="var(--slate)"/>
    </svg>
    <p class="flap-name">Velqoran</p>
  </section>

  <!-- Envelope, front -->
  <section class="sheet envelope-front" aria-label="Briefumschlag Vorderseite">
    <div class="brand">
      <span class="brand-square"></span>
      <div class="brand-text">
        <span class="brand-name">Velqoran</span>
        <span class="brand-tag">Personalberatung</span>
      </div>
    </div>
    <ul class="contact-list" style="color:#111">
      <li><svg><use href="#icon-phone"/></svg>+49 01 2345 6789</li>
      <li><svg><use href="#icon-globe"/></svg>www.velqoran.de</li>
      <li><svg><use href="#icon-mail"/></svg>post@velqoran.de</li>
    </ul>
    <svg class="swoosh" viewBox="0 0 1141 210" preserveAspectRatio="none" aria-hidden="true">
      <path d="M0 172 Q560 192 1141 72 L1141 210 L0 210 Z" fill="var(--teal)"/>
      <path d="M290 166 Q760 144 1141 4 L1141 60 Q760 154 290 166 Z" fill="var(--slate)"/>
    </svg>
  </section>

</main>
</body>
</html>
```